Coffee roastery and coffee shop needs a packaging design

We need a packaging design for an our company we sell coffee beans for coffee shops . and we have a coffee shop . our company name is (BRAMBLE ROASTERY) we are based in UAE. We want a cup design for cold coffee and hot and coffee bag design and paper bag design. I uploaded our logo design.

```html
<!DOCTYPE html>
<html lang="en">
<head>
<meta charset="utf-8">
<title>Bramble Roastery – Coffee Bag Label</title>
<link rel="stylesheet" href="https://fonts.googleapis.com/css2?family=Michroma&family=Montserrat:wght@300;400&display=swap">
<style>
  :root {
    --canvas: #ffffff;
    --band-red: #c61a24;
    --panel-light: #e9ebec;
    --panel-lighter: #f8f8f8;
    --ink: #2b2b2b;
    --ink-soft: #555555;
    --brush-green-dark: #86ad69;
    --brush-green: #aec27c;
    --brush-green-light: #cfd9a8;
    --brush-tan: #c4bc94;
    --branch-green: #7cc49a;
    --berry-red: #b8474f;
    --bean-brown: #a88a72;
    --bean-gold: #e3cd87;
    --leaf-green: #d6e6a8;
    --white: #ffffff;
  }
  * { box-sizing: border-box; margin: 0; padding: 0; }
  html, body {
    width: 1200px; height: 1200px; overflow: hidden;
    background: var(--canvas);
  }
  .label {
    position: absolute; left: 110px; top: 28px;
    width: 980px; height: 1144px;
  }
  .label__band {
    position: absolute; left: 0; top: 0;
    width: 227px; height: 100%;
    background: var(--band-red);
  }
  .band__name {
    position: absolute; left: 0; top: 848px; width: 227px;
    text-align: center;
    font-family: "Michroma", sans-serif; font-size: 10px;
    letter-spacing: 2px; color: var(--white);
  }
  .label__panel {
    position: absolute; left: 227px; top: 0;
    width: 753px; height: 100%;
    background: linear-gradient(135deg, var(--panel-light) 0%, var(--panel-lighter) 70%, var(--white) 100%);
    overflow: hidden;
  }
  .art { position: absolute; }
  .art--branch {
    left: 40px; top: 0; width: 260px; height: 210px;
    background: linear-gradient(150deg, var(--branch-green) 0%, var(--branch-green) 35%, var(--berry-red) 100%);
    border-radius: 0 0 140px 20px;
    opacity: .55;
  }
  .art--brush {
    left: 0; top: 150px; width: 753px; height: 387px;
    background: linear-gradient(180deg, var(--brush-green-dark) 0%, var(--brush-green) 35%, var(--brush-green-light) 65%, var(--brush-tan) 85%, var(--brush-green) 100%);
    border-radius: 40px 8px 60px 30px;
    opacity: .92;
  }
  .art--beans {
    left: 330px; top: 480px; width: 110px; height: 330px;
    background: linear-gradient(180deg, var(--berry-red) 0%, var(--bean-brown) 30%, var(--bean-gold) 55%, var(--bean-brown) 100%);
    border-radius: 55px;
    opacity: .45;
  }
  .art--leaf {
    left: 575px; top: 895px; width: 178px; height: 249px;
    background: linear-gradient(160deg, rgba(214,230,168,.35), var(--leaf-green));
    border-radius: 60% 10% 60% 10%;
  }
  .brand-name {
    position: absolute; left: 0; width: 753px; top: 375px;
    text-align: center;
    font-family: "Michroma", sans-serif; font-size: 24px;
    letter-spacing: 6px; color: var(--ink);
  }
  .badge {
    position: absolute; left: 133px; top: 755px; width: 70px; height: 70px;
  }
  .badge__note {
    position: absolute; left: 88px; width: 160px; top: 830px;
    text-align: center;
    font-family: "Montserrat", sans-serif; font-weight: 300; font-size: 10px;
    color: var(--ink-soft);
  }
  .product {
    position: absolute; left: 234px; width: 300px; top: 855px;
    text-align: center; color: var(--ink);
  }
  .product__sub {
    font-family: "Montserrat", sans-serif; font-weight: 300; font-size: 17px;
  }
  .product__title {
    font-family: "Michroma", sans-serif; font-size: 35px; letter-spacing: 4px;
    line-height: 1.1;
  }
  .methods {
    position: absolute; left: 264px; top: 932px; width: 250px;
    display: flex; justify-content: space-between;
  }
  .method {
    width: 58px; text-align: center;
    font-family: "Montserrat", sans-serif; font-weight: 300; font-size: 9px;
    color: var(--ink-soft);
  }
  .method svg { display: block; margin: 0 auto 6px; width: 28px; height: 28px; }
  .weight {
    position: absolute; left: 234px; width: 300px; top: 1026px;
    text-align: center;
    font-family: "Michroma", sans-serif; font-size: 18px; letter-spacing: 3px;
    color: var(--ink);
  }
</style>
</head>
<body>
  <main class="label">
    <div class="label__band">
      <p class="band__name">BRAMBLE ROASTERY</p>
    </div>
    <section class="label__panel">
      <div class="art art--branch" role="img" aria-label="Line drawing of a coffee branch with red cherries"></div>
      <div class="art art--brush" role="img" aria-label="Green painted brush strokes"></div>
      <p class="brand-name">BRAMBLE ROASTERY</p>
      <div class="art art--beans" role="img" aria-label="Scattered coffee beans in brown, gold, green and red falling down"></div>

      <svg class="badge" viewBox="0 0 70 70" aria-hidden="true">
        <circle cx="35" cy="35" r="32" fill="var(--ink)"/>
        <circle cx="35" cy="35" r="27" fill="var(--white)"/>
        <circle cx="35" cy="35" r="20" fill="var(--ink)"/>
      </svg>
      <p class="badge__note">PRODUCED IN THE UAE</p>

      <div class="product">
        <p class="product__sub">ROASTED AND GROUND</p>
        <p class="product__title">COFFEE</p>
      </div>

      <div class="methods">
        <div class="method">
          <svg viewBox="0 0 28 28" aria-hidden="true"><path d="M4 8 H24 L16 20 H12 Z M10 22 H18" fill="none" stroke="var(--ink)" stroke-width="1.5"/></svg>
          FILTER
        </div>
        <div class="method">
          <svg viewBox="0 0 28 28" aria-hidden="true"><circle cx="8" cy="9" r="4" fill="none" stroke="var(--ink)" stroke-width="1.5"/><path d="M11 12 L25 22" stroke="var(--ink)" stroke-width="3" stroke-linecap="round"/></svg>
          ESPRESSO
        </div>
        <div class="method">
          <svg viewBox="0 0 28 28" aria-hidden="true"><path d="M14 2 V6 M10 6 H18 M9 8 H19 V25 H9 Z M19 11 H22 V20 H19" fill="none" stroke="var(--ink)" stroke-width="1.5"/></svg>
          PLUNGER
        </div>
        <div class="method">
          <svg viewBox="0 0 28 28" aria-hidden="true"><ellipse cx="11" cy="10" rx="4" ry="6" fill="var(--ink)"/><ellipse cx="18" cy="19" rx="4" ry="6" fill="var(--ink)"/></svg>
          BEANS
        </div>
      </div>

      <p class="weight">400G</p>
      <div class="art art--leaf" role="img" aria-label="Pale green painted leaf outline"></div>
    </section>
  </main>
</body>
</html>
```